Webdesign for recipe site

Please take a look at www.pfannenhaus.com. PH is a community site with around 60000 user recipes. It is a one-man-project and needs a redesign.
The new design shall meet these facts
high usability
1st focus on content
2nd focus on search and registration-elements
flat menü ? much content above the fold
well contured font type, size and color
coherent button, box and element design
useful design guide for the whole site
flexible font-sizes (changable css)
flexible color set for day and night mode (changable css)
And these facts shall not change
Keeping the „soul“ of pfannenhaus. PH is an independent and free recipe source. No media corporation. Everyone can participate.
This means, that PH is seen as a very personal, even private website and the design shall transport this. The design shall not be cold or heartless. It shall work and leave a cheerful impression as well. The design shall keep the atmosphere of a one-man-project, where everyone is welcomed and the personal touch is warm and heartly.
Since 8 years, the major color is red. The tone must be kept while the intensitity shall be lowered. A decent background and a warm and welltought color set are wanted in a way, that the tone of the website is still seen as red. Probably the links shall remain red, that way the rest can be set less intense.
And these facts are open
The design elements are the cook and the red tomato. While it would be nice to keep the cook (not required at any means), the tomato could be dropped. If they fit into a new design – great, if not, it's ok.
Example Pages
Recipe: http://www.pfannenhaus.com/r/68765-panini-vereinfachte-variation.html
Category: http://www.pfannenhaus.com/kb/0k0/Backrezept/rezepte.html
Homepage: http://www.pfannenhaus.com
Updates
A nice color set: http://www.artquorra.com/design/463831
A well structured design: http://www.artquorra.com/design/452858
Reason: Just 3 days left and no submission yet.
We will guarantee the project payment (thanks for hinting, Tavin) and extend the deadline by 7 days.
Thank you for your submissions.
The brown/red/beige color-sets are good, they lead the way. The layout though is mostly too playful. It shall be clean and simple and likely to fit for all the content, for the single recipe as well as the recipe lists, the profile page and the homepage.
I got inspired by you color sets and set up a testpage that pretty much goes in to the direction I want. Very flat header, peaceful and warm colors, no distraction, focus on the content. What's still missing is the breadcrumb section and an idea to fill the homepage and the recipe lists. And probably the colors (especially the light background-color, is it beige?) can also be better choosen.
Please see http://www.pfannenhaus.com/test-543677423/r_v01.html
Kind regards, Lukas
Reason: I extend the deadline once more to give Volbrin Designs the opportunity to participate. It would be nice to see drafts that go more into the clean and simple direction as I updated in the brief. Here is the current status: http://www.pfannenhaus.com/r/60262-steak-auf-spargel.html (is on test now). Maybe the beige-colors can be choosen more cleaner and suggestions for the homepage and recipe lists and the footer are very welcome also. Looking forward for your designs!
I'll put the Feedback on the latest design of quietmaple in the brief, so you all find it.
http://www.artquorra.com/design/587249/web-design-by-quietmaple
-
Dont't know man, this still doesn't look as clean as I need it. There are 100s of recipe sites online and it is urgent to design the page with clear focus on the content. As little distraction as possible, there will be ads for that.
Mainly, you did too much. There are too many design elements and the round bites with the squares. The header shall be as small as in the mentioned page: http://www.pfannenhaus.com/r/60262-steak-auf-spargel.html
I show you an example of a clean page as I see it: http://www.webtalvo.org/q/ips-and-domains
These are not the colors I want but they all fit together. I also need the font larger and the basic color scheme must be warmer. But maybe you can understand where I'm going or where I want to go.
Please do it very simple, with no corners, as flat and clean as possible, with a genuine feeling on first site of where the content is, what the focus of the site is (content).
Thank's.
Target Market(s)
age 35-55, majority is female, interested in recipes, cooking, baking
Industry/Entity Type
Media
Look and feel

```html
<!DOCTYPE html>
<html lang="de">
<head>
<meta charset="utf-8">
<title>Pfannenhaus – Rezepte tauschen</title>
<link rel="stylesheet" href="https://fonts.googleapis.com/css2?family=Noto+Sans:wght@400;700&family=Open+Sans:wght@400;600&display=swap">
<style>
:root{
  --page-bg:#f7f1dc;
  --sheet:#ffffff;
  --brand-red:#a8141b;
  --ribbon:#8b1313;
  --ribbon-dark:#5e0a0a;
  --link:#a33a14;
  --heading-red:#8a2a10;
  --rust:#a6401c;
  --cream:#fdf8ea;
  --taupe:#c4b49f;
  --taupe-light:#f6efe4;
  --taupe-border:#c8b6a2;
  --muted:#8a7f72;
  --text:#1f1a17;
  --comment-bg:#efefef;
  --footer:#7a2a13;
}
*{box-sizing:border-box;margin:0;padding:0}
html,body{width:959px;height:1200px;overflow:hidden}
body{background:var(--page-bg);font-family:"Noto Sans",Verdana,sans-serif;font-size:11px;color:var(--text);position:relative}
a{color:var(--link);text-decoration:none}
ul{list-style:none}
.abs{position:absolute}
.sheet{position:absolute;left:68px;top:0;width:828px;height:1200px;background:var(--sheet)}
.h-serif{font-family:"Open Sans",Verdana,sans-serif}

/* header */
.logo{left:100px;top:36px;display:flex;align-items:center;gap:10px;color:var(--brand-red);font-family:"Open Sans",sans-serif;font-weight:600;font-size:40px;line-height:1}
.logo-dot{width:26px;height:26px;border-radius:50%;background:var(--brand-red)}
.toplinks{top:18px;left:634px;font-size:12px;color:var(--text);display:flex;gap:0}
.toplinks span{margin-right:14px}
.search-field{left:630px;top:49px;width:170px;height:26px;border:1px solid #cfcfcf;background:#f2f2f2}
.search-label{left:808px;top:54px;font-size:15px;font-weight:700;color:var(--brand-red)}
.nav{left:0;top:100px;width:959px;height:52px}
.nav-items{left:52px;top:103px;width:858px;height:42px;display:flex;align-items:center;color:#fff;font-size:15px;font-weight:700;font-family:"Open Sans",sans-serif}
.nav-items span{position:absolute;top:11px}

/* hero */
.photo{background:linear-gradient(135deg,#7a4a22,#c8763a 40%,#e0b070 60%,#6b4020);border:3px solid #eee}
.intro-title{left:362px;top:173px;font-size:17px;color:var(--heading-red)}
.intro-text{left:362px;top:205px;width:305px;line-height:16.5px;text-align:justify}
.intro-links{left:362px;top:310px;line-height:18px}
.box-day{left:681px;top:181px;width:205px;height:198px;border:1px solid var(--taupe-border);background:linear-gradient(#f8f1e8,#cbb9a4);padding:12px 9px}
.box-day h3{font-weight:400;font-size:13px;line-height:17px;color:var(--heading-red);margin-bottom:17px}
.box-day p{line-height:17px;text-align:justify}
.btn-row{left:724px;top:340px;display:flex;font-size:11px}
.btn-row span{padding:0 3px;height:15px;line-height:14px;border:1px solid var(--brand-red)}
.btn-light{background:#fff;color:var(--brand-red)}
.btn-dark{background:var(--brand-red);color:#fff}

/* feature */
.bar{left:79px;width:597px;color:#fff;font-size:16px;font-family:"Open Sans",sans-serif;padding-left:10px}
.bar-rust{top:395px;height:30px;line-height:30px;background:var(--rust)}
.feature{left:79px;top:425px;width:597px;height:160px;background:var(--cream)}
.feature-list{left:328px;top:443px;line-height:16px}
.feature-more{left:328px;top:539px;width:330px;line-height:16.5px;color:var(--text)}
.box-best{left:681px;top:399px;width:205px;height:332px;border:1px solid var(--taupe-border);background:linear-gradient(#f5ede2 0,#d9c9b6 130px,var(--taupe) 140px);padding:12px 10px}
.box-best h3{font-weight:400;font-size:17px;margin-bottom:2px}
.box-best li,.box-best .more{line-height:15.8px}
.thumb{width:88px;height:88px;border:2px solid #fff}

/* lists */
.sec-title{font-size:17px;font-family:"Open Sans",sans-serif;font-weight:400}
.new-recipes{left:89px;top:600px}
.new-recipes .sec-title{color:var(--muted)}
.forum{left:366px;top:600px}
.list{margin-top:6px;line-height:16px}
.more-line{position:absolute;top:706px;color:var(--text)}

/* magazine */
.bar-taupe{top:739px;height:31px;line-height:31px;background:var(--taupe)}
.mag-text{line-height:16.5px}
.pager{left:609px;top:893px;display:flex;gap:2px;font-size:9px;font-weight:700;color:var(--heading-red);background:#f1ece4;padding:1px 6px;border-radius:3px}
.pager span{padding:0 3px}
.box-season{left:684px;top:750px;width:203px;height:170px;border:1px solid var(--taupe-border);padding:4px 8px}
.box-season h3{font-weight:400;font-size:17px;color:#5a4f44;margin-bottom:4px;font-family:"Open Sans",sans-serif}
.box-season .links a{display:block;line-height:18px;padding-left:3px}
.box-season hr{border:0;border-top:1px dotted #999;margin:6px -8px 6px}
.box-season .links-grey span{display:block;line-height:14.5px;color:#6b6560;padding-left:3px}

/* comments */
.comments-title{left:89px;top:928px;color:#5a4f44}
.select{top:936px;height:15px;border:1px solid var(--brand-red);background:#fff;font-size:10px;line-height:13px;padding-left:3px}
.select::after{content:"";position:absolute;right:1px;top:1px;width:13px;height:11px;background:#ddd;border-left:1px solid #999}
.comment{background:var(--comment-bg);padding:5px 4px;line-height:14px}
.comment .who{color:var(--link)}

/* footer */
.footer{left:68px;top:1090px;width:828px;height:110px;background:var(--footer);border-top:3px dotted #a85a40}
.foot-col{color:#fff;line-height:12.7px;top:1109px}
</style>
</head>
<body>
<div class="sheet"></div>

<!-- header -->
<div class="abs logo"><span class="logo-dot"></span>pfannenhaus</div>
<div class="abs toplinks"><span>Login</span><span>| Kostenlos Registrieren</span><span style="margin-left:12px">Hilfe</span></div>
<div class="abs search-field"></div>
<div class="abs search-label">search</div>

<svg class="abs nav" width="959" height="52" viewBox="0 0 959 52">
  <polygon points="5,22 40,8 66,8 66,48 40,48" fill="var(--ribbon-dark)"/>
  <polygon points="954,22 920,8 892,8 892,48 920,48" fill="var(--ribbon-dark)"/>
  <rect x="52" y="3" width="858" height="42" fill="var(--ribbon)"/>
  <rect x="52" y="3" width="858" height="4" fill="#a52020"/>
  <g stroke="#e8c8c8" stroke-width="1.5" stroke-dasharray="2 3">
    <line x1="200" y1="14" x2="200" y2="36"/><line x1="333" y1="14" x2="333" y2="36"/>
    <line x1="466" y1="14" x2="466" y2="36"/><line x1="587" y1="14" x2="587" y2="36"/>
    <line x1="771" y1="14" x2="771" y2="36"/>
  </g>
</svg>
<nav class="abs nav-items">
  <span style="left:76px">Start</span><span style="left:190px">Rezepte</span><span style="left:326px">Magazin</span>
  <span style="left:455px">Foren</span><span style="left:578px">Gemeins chaft</span><span style="left:763px">Market</span>
</nav>

<!-- intro -->
<div class="abs photo" role="img" aria-label="Foto eines überbackenen Gemüseauflaufs" style="left:80px;top:170px;width:262px;height:215px"></div>
<h1 class="abs intro-title h-serif" style="font-weight:400">Rezepte tauschen? Pfannenhaus!</h1>
<p class="abs intro-text">Du liebst gute Rezepte? Willkommen bei Pfannenhaus. Hier findest du tausende Rezepte, viele mit Bild. Du kannst jedes Rezept speichern und kommentieren. Und du kannst sofort deine eigenen Rezepte und Bilder hochladen. Ohne Wartezeiten. Los geht's.</p>
<div class="abs intro-links"><a>-&gt; Registrieren</a><br><a>-&gt; Rezepte finden</a><br><a>-&gt; Rezept eintragen</a></div>

<aside class="abs box-day">
  <h3>Feuriger Chilitopf aus dem Ofen Zutaten:</h3>
  <p>1 Kidneybohnen (425ml), 1 Maiskörner (425ml), 2 Bd Lauchzwiebeln, 1 kg Gulasch, gemischt, 3 EL Öl, Salz, schwarzer Pfef... · <b>zum Rezept</b></p>
</aside>
<div class="abs btn-row"><span class="btn-light">Rezept des Tages</span><span class="btn-dark">Abonnieren</span></div>

<!-- feature -->
<div class="abs bar bar-rust">Feldsalat &amp; Grünkohl</div>
<div class="abs feature"></div>
<div class="abs photo" role="img" aria-label="Foto eines Feldsalats mit Champignons auf einem Teller" style="left:89px;top:440px;width:219px;height:127px;border:0;background:linear-gradient(135deg,#6a6a6a,#4f8a2a 45%,#8cbf45 60%,#5a5a5a)"></div>
<ul class="abs feature-list">
  <li>- Marlenes Feldsalat mit Champis</li>
  <li>- Grünkohl mit Pinkel und Hamburger süßen Kartoffeln</li>
  <li>- Gebratener Rosenkohl</li>
  <li>- Vogerlsalat mit Himbeeren und Speck</li>
  <li>- Chicoree im Strudelteig</li>
</ul>
<p class="abs feature-more"><a>und außerdem alle Rezepte für Feldsalat</a> (202), <a>Grünkohl</a> (102), <a>Rosenkohl</a> (188), <a>Chicoree</a> (164), <a>und Pastinaken</a> (54)</p>

<aside class="abs box-best">
  <h3 class="h-serif">Das Beste vom Tage</h3>
  <ul>
    <li>- Schichtsalat mit Thunfisch</li><li>- Die magische Kohlsuppe</li><li>- Waffel - Grundrezept</li>
    <li>- Österreichischer Kaiserschmarrn</li><li>- Apfel - Pudding - Strudel</li>
  </ul>
  <div class="more">mehr &gt;</div>
</aside>
<div class="abs thumb" role="img" aria-label="Foto einer Obsttorte" style="left:694px;top:538px;background:linear-gradient(#e06a20,#f0c090 60%,#e8e0d0)"></div>
<div class="abs thumb" role="img" aria-label="Foto einer Suppe in oranger Schüssel" style="left:787px;top:538px;background:radial-gradient(#e8d090 35%,#e07a30 60%,#c0c8c0)"></div>
<div class="abs thumb" role="img" aria-label="Foto eines Stücks Apfelkuchen" style="left:694px;top:631px;background:linear-gradient(135deg,#6a5a40,#e8c060 50%,#f4e8d0)"></div>
<div class="abs thumb" role="img" aria-label="Foto eines Gemüseauflaufs" style="left:787px;top:631px;background:linear-gradient(135deg,#7a4a22,#d07a3a 45%,#e0b070 65%,#6b4020)"></div>

<!-- lists -->
<section class="abs new-recipes">
  <h2 class="sec-title">Neue Rezepte</h2>
  <ul class="list"><li><a>Papayacreme</a></li><li><a>Überraschungs-Wickel</a></li><li><a>Koteletts auf bayerische Art</a></li><li><a>Apfel - Pudding - Strudel</a></li><li><a>gefüllter Leberkäse mit Kartof...</a></li></ul>
</section>
<span class="more-line" style="left:158px">weitere neue Rezepte</span>
<section class="abs forum">
  <h2 class="sec-title">Aktuell in den Foren</h2>
  <ul class="list"><li><a>1. Neues Spiel: Ahnungen</a></li><li><a>2. ein kleines Spiel...</a></li><li><a>3. IN und OUT des Tages</a></li><li><a>4. Melde mich für eine Zeit mal ab ...</a></li><li><a>5. Was kocht Ihr denn heute?</a></li></ul>
</section>
<span class="more-line" style="left:453px">weitere aktuelle Forenbeiträge</span>

<!-- magazine -->
<div class="abs bar bar-taupe">Neu im Magazin</div>
<div class="abs photo" role="img" aria-label="Foto eines Kuchenstücks" style="left:79px;top:797px;width:92px;height:66px;border:0;background:linear-gradient(135deg,#6a5a40,#e8c060 50%,#f4e8d0)"></div>
<div class="abs mag-text" style="left:186px;top:787px;width:225px">Pitahaya - was ist das nun wieder?<br><br style="line-height:10px">Ab Mitte Dezember gibt es in den Super-märkten bei den Exoten wieder Pitahayas. Was ist das eigentlich für eine Frucht?</div>
<div class="abs mag-text" style="left:438px;top:783px;width:235px">Wer hat das Weihnachtsplätzchen erfunden?<br><br style="line-height:10px">Wer kam eigentlich als erster auf die Idee, zu Weihnachten leckere Plätzchen zu backen.</div>
<div class="abs pager"><span>1</span><span>2</span><span>3</span><span>4</span></div>

<aside class="abs box-season">
  <h3>Aktuelle Saisonrezepte</h3>
  <div class="links"><a>Suchwerk-Anzeigen</a><a>Rührmax Rezepte</a><a>Salat Rezept</a><a>Rezepte Fisch</a></div>
  <hr>
  <div class="links-grey"><span>Rotkohl Rezepte</span><span>Rosenkohl Rezepte</span><span>Meerrettich Rezepte</span></div>
</aside>

<!-- comments -->
<h2 class="abs sec-title comments-title">Aktuelle Kommentare</h2>
<div class="abs select" style="left:724px;width:111px">alle</div>
<div class="abs select" style="left:839px;width:37px">10</div>
<div class="abs comment" style="left:79px;top:962px;width:390px;height:43px"><div class="who">Backfee88 zu Tomatensalat mit geschmorten Zwiebeln</div>Das hätte ich auch gerne gewußt</div>
<div class="abs comment" style="left:481px;top:959px;width:390px;height:43px"><div class="who" style="padding-left:15px">kochtante_eva zu Schweinebauch mit Semmelfülle</div><div style="padding-left:15px">Kein Mehl dazugeben, nur Eier verwenden, kannst auch das Eiweiß zu Schneeschlagen und locker unterheben</div></div>
<div class="abs comment" style="left:79px;top:1018px;width:390px;height:43px"><div class="who">Backfee88 zu Tomatensalat mit geschmorten Zwiebeln</div><div style="padding-left:13px">Das hätte ich auch gerne gewußt</div></div>
<div class="abs comment" style="left:483px;top:1017px;width:388px;height:43px"><div class="who" style="padding-left:10px">Backfee88 zu Tomatensalat mit geschmorten Zwiebeln</div><div style="padding-left:12px">Das hätte ich auch gerne gewußt</div></div>

<!-- footer -->
<footer class="abs footer"></footer>
<div class="abs foot-col" style="left:100px">Newsletter<br>RSS: Rezept des Tages<br>RSS: Neue Rezepte</div>
<div class="abs foot-col" style="left:324px;top:1105px">Impressum | Kontakt<br>Team | Urheberrecht<br>AGB | Regeln<br>Hier werben | Stats<br>Externe Nutzung<br>Surftipps:</div>
<div class="abs foot-col" style="left:514px;top:1106px">Cocktails<br>Sporttreff<br>Espressomaschine<br>www.feinherd.at<br>Herdmeisterei</div>
</body>
</html>
```